Banner images for web site

Four banner images for Home page of BrightLedgerWorks.com:

Max Width: 575px
Min Width: 550px

Min Height: 300px
Max Height: 250px

Image 1: Use picture of someone swiping a Credit/debit card
Main Text: INNOVATIVE, EFFICIENT AND COST EFFECTIVE CARD PROCESSING SOLUTIONS.
Caption/Call to action text/button: GET STARTED NOW

Image 2: (Use attached picture)
Main Text: ATM PROCESSING, ATM TRANSACTION REPORTING AND ATM ONLINE ACCESS.

Image3: (Use attached picture)
Main Text: WE LISTEN, WE CARE AND WE ARE HERE FOR YOU 24/7.
Caption/Call to action text/button: GET HELP NOW

Image4: (Use picture of middle age, mix race(Black, white, etc) and gender) dressed in business casual or formal business
Main Text: BUILD YOUR CAREER, LIVE YOUR DREAM.
Caption/Call to action text/button: JOIN OUR TEAM

Note: be mindful of our company colors (Green and brown as can be seen at our website)

The idea is to create a sliding banner like the following:
http://www.cardivio.us/

The Text in bold on the left, and an illustrative image on the right with slightly fading effect
Updates

Project Deadline Extended
Reason: Other parts of this project have been pushed back so I am extending this deadline by 3 days.

A reminder that this project is simply about images for a slider on the website. I have provided most of the background images to use for that.

We just need it to be expressive, clean and Bold. Use modern, not boring fonts.

Thanks

Project Deadline Extended
Reason: No good design received. Only two designers so far. We need more designs

Target Market(s)

Small merchants, store owners, groceries, restaurants, etc

Industry/Entity Type

Business

Requirements
Must have
• Just banners like the onbes used on this site;
http://www.cardivio.us/

```html
<!DOCTYPE html>
<html lang="en">
<head>
<meta charset="utf-8">
<title>BrightLedgerWorks.com – Card Processing Banner</title>
<link rel="stylesheet" href="https://fonts.googleapis.com/css2?family=Archivo:wdth,wght@125,800&family=Arimo:wght@400;700&display=swap">
<style>
  :root {
    --page-bg: #f8f8f8;
    --frame: #d9d9d9;
    --panel: rgba(40, 34, 30, 0.62);
    --accent-green: #c9f7a2;
    --accent-orange: #f6a900;
    --text-light: #ffffff;
    --button-green: #479a24;
    --button-green-dark: #357a18;
  }
  * { box-sizing: border-box; margin: 0; padding: 0; }
  html, body {
    width: 1200px;
    height: 1000px;
    overflow: hidden;
    background: var(--page-bg);
  }
  .banner {
    position: absolute;
    left: 312px;
    top: 348px;
    width: 577px;
    height: 304px;
    border: 2px solid var(--frame);
    border-radius: 5px;
    overflow: hidden;
  }
  .banner-photo {
    position: absolute;
    inset: 0;
    background:
      radial-gradient(ellipse 160px 110px at 120px 40px, rgba(214,150,120,0.85), rgba(214,150,120,0) 70%),
      radial-gradient(ellipse 140px 120px at 420px 70px, rgba(170,110,55,0.85), rgba(170,110,55,0) 75%),
      radial-gradient(ellipse 160px 120px at 460px 230px, rgba(120,128,110,0.9), rgba(120,128,110,0) 75%),
      linear-gradient(90deg, #c9b39a 0%, #b7a58e 30%, #a89a92 48%, #b4b0a0 65%, #9d9a86 80%, #bfc3ac 100%);
  }
  .banner-panel {
    position: absolute;
    left: 0;
    top: 96px;
    width: 243px;
    height: 171px;
    background: linear-gradient(90deg, var(--panel) 0%, var(--panel) 70%, rgba(40,34,30,0.35) 100%);
  }
  .headline {
    position: absolute;
    left: 19px;
    top: 114px;
    font-family: "Arimo", Helvetica, Arial, sans-serif;
    font-size: 20px;
    line-height: 18px;
    color: var(--text-light);
    letter-spacing: -0.2px;
  }
  .headline .strong {
    font-family: "Archivo", "Arial Black", sans-serif;
    font-stretch: 125%;
    font-weight: 800;
    font-size: 21px;
    letter-spacing: 0.3px;
  }
  .headline .innovative { color: var(--accent-green); }
  .headline .cost { color: var(--accent-orange); }
  .headline .comma { color: var(--accent-green); }
  .cta {
    position: absolute;
    left: 16px;
    top: 220px;
    width: 149px;
    height: 28px;
    border-radius: 4px;
    background: linear-gradient(180deg, #52a92c, var(--button-green-dark));
    color: var(--text-light);
    font-family: "Arimo", Helvetica, Arial, sans-serif;
    font-weight: 700;
    font-size: 12px;
    letter-spacing: -0.2px;
    display: flex;
    align-items: center;
    justify-content: center;
    box-shadow: 0 1px 2px rgba(0,0,0,0.3);
  }
</style>
</head>
<body>
  <section class="banner">
    <div class="banner-photo" role="img" aria-label="Photo of a customer swiping a credit card through a payment terminal at a store checkout"></div>
    <div class="banner-panel"></div>
    <h1 class="headline">
      <span class="strong innovative">Innovative</span><span class="comma">,</span><br>
      Efficient and<br>
      <span class="strong cost">Cost Effective</span><br>
      Card Processing<br>
      Solutions
    </h1>
    <div class="cta">GET STARTED NOW !</div>
  </section>
</body>
</html>
```